Harbourline Green Jack Socials - Flyer

So now that i have the logo, I need a flyer made up for printing to be delivered to businesses and residential homes.
Below is some information that I want included in the design, in any order and in anyway.
What better way to spend time with family, friends or workmates then to enjoy 2 hours of barefoot bowls.
We can cater for Xmas Parties, Buck's and Hen's Parties, Birthday Parties, Team Building events.
We have food and drink packages to suit all your needs.
So why not come along and have the best fun you can have on 2 feet!
We have 2 locations at Wendlebrook Sports and Bowling Club and Mossvale Ridge Bowling Club
Prices start from $12pp for 2 hours of lawn bowls fun
Contact Colin Parrow on 0478 615 240 or visit our website www.greenjacksocials-example.com.au for more information and to enquire about your function today!

```html
<!DOCTYPE html>
<html lang="en">
<head>
<meta charset="utf-8">
<title>Harbourline Green Jack Socials - Flyer</title>
<link rel="stylesheet" href="https://fonts.googleapis.com/css2?family=Arimo:wght@700&display=swap">
<style>
  :root {
    --red: #e3202c;
    --red-dark: #b5121b;
    --pink: #ec2352;
    --blue: #1f6fc1;
    --blue-dark: #124f91;
    --green: #39a935;
    --green-dark: #1f7d22;
    --lime: #9fd13a;
    --white: #ffffff;
    --ink: #1c1c1c;
  }
  html, body { margin: 0; padding: 0; overflow: hidden; }
  body { width: 849px; height: 1200px; background: var(--white); }
  .flyer {
    position: relative; width: 849px; height: 1200px; overflow: hidden;
    font-family: "Arimo", Arial, sans-serif; font-weight: 700;
  }
  .scene-photo {
    position: absolute; inset: 0;
    background:
      radial-gradient(ellipse at 50% 20%, #a9d46a 0%, rgba(169,212,106,0) 55%),
      linear-gradient(180deg, #6fae3a 0%, #4f9429 35%, #79b842 55%, #c7e3a0 78%, #f4faee 100%);
  }
  .headline {
    position: absolute; left: 18px; top: 10px; width: 813px; height: 158px;
    box-sizing: border-box; padding: 14px 26px;
    background: linear-gradient(180deg, #f23a3f, var(--red-dark));
    border-radius: 22px; color: var(--white);
    font-size: 40px; line-height: 1.15; text-align: center;
    display: flex; align-items: center; justify-content: center;
    box-shadow: 0 4px 10px rgba(0,0,0,.35);
  }
  .bubble {
    position: absolute; box-sizing: border-box; border-radius: 22px;
    color: var(--white); text-align: center; font-size: 21px; line-height: 1.25;
    display: flex; align-items: center; justify-content: center;
    box-shadow: 0 3px 8px rgba(0,0,0,.3);
  }
  .bubble-tail { position: absolute; }
  .bubble-events {
    left: 28px; top: 492px; width: 378px; height: 148px; padding: 12px 18px;
    background: linear-gradient(180deg, #2d86d8, var(--blue-dark));
  }
  .bubble-fun {
    left: 462px; top: 466px; width: 360px; height: 108px; padding: 10px 16px;
    background: linear-gradient(180deg, #4fbf3f, var(--green-dark));
  }
  .note {
    position: absolute; box-sizing: border-box; border-radius: 20px;
    text-align: center; font-size: 21px; line-height: 1.25;
    display: flex; align-items: center; justify-content: center;
  }
  .note-locations {
    left: 42px; top: 700px; width: 342px; height: 150px; padding: 10px 14px;
    background: var(--white); color: var(--red);
    border: 3px dotted var(--red);
  }
  .note-food {
    left: 452px; top: 692px; width: 370px; height: 90px; padding: 8px 14px;
    background: var(--white); color: var(--green-dark);
    border: 3px dotted var(--green);
  }
  .price-tag {
    position: absolute; left: 550px; top: 804px; width: 258px; height: 132px;
    box-sizing: border-box; padding: 10px 12px; border-radius: 16px;
    background: linear-gradient(180deg, #f23a3f, var(--red-dark));
    color: var(--white); font-size: 23px; line-height: 1.25; text-align: center;
    display: flex; align-items: center; justify-content: center;
    box-shadow: 0 3px 8px rgba(0,0,0,.3);
  }
  .contact {
    position: absolute; left: 40px; top: 948px; width: 769px; height: 228px;
    box-sizing: border-box; padding: 14px 20px; border-radius: 26px;
    background: rgba(255,255,255,.82);
    color: var(--pink); font-size: 34px; line-height: 1.2; text-align: center;
    display: flex; align-items: center; justify-content: center;
  }
</style>
</head>
<body>
<main class="flyer">
  <div class="scene-photo" role="img" aria-label="Close-up photo of bare feet on a lawn bowling green with bowls rolling across the grass"></div>

  <h1 class="headline" style="margin:0;">What better way to spend time with family, friends or workmates then to enjoy 2 hours of barefoot bowls.</h1>

  <div class="bubble bubble-events">We can cater for Xmas Parties, Buck's and Hen's Parties, Birthday Parties, Team Building events.</div>
  <svg class="bubble-tail" style="left:300px;top:636px" width="60" height="42" viewBox="0 0 60 42" aria-hidden="true">
    <path d="M0 0 H44 L58 40 Z" fill="var(--blue-dark)"/>
  </svg>

  <div class="bubble bubble-fun">So why not come along and have the best fun you can have on 2 feet!</div>
  <svg class="bubble-tail" style="left:492px;top:570px" width="50" height="36" viewBox="0 0 50 36" aria-hidden="true">
    <path d="M6 0 H44 L0 34 Z" fill="var(--green-dark)"/>
  </svg>

  <p class="note note-locations" style="margin:0;">We have 2 locations at Wendlebrook Sports and Bowling Club and Mossvale Ridge Bowling Club</p>

  <p class="note note-food" style="margin:0;">We have food and drink packages to suit all your needs.</p>

  <p class="price-tag" style="margin:0;">Prices start from $12pp for 2 hours of lawn bowls fun</p>

  <p class="contact" style="margin:0;">Contact Colin Parrow on 0478 615 240 or visit our website www.greenjacksocials-example.com.au for more information and to enquire about your function today!</p>
</main>
</body>
</html>
```